Business Card Design Project

i have the logo designed.
I require designs for the managing director and the general manager.
we need space for email, and a mobile number.
any other cool stuff/design you guys just let me see what you got.
The managing director card could be black, minimalist, and the cards for the rest of the company could be using the green logo.
it has to impress. transportation market is fragmented, we want to appear professional and sophisticated.
Md: Tariq walid hussain
General manager: nabil hussain
Target Market(s)
clients: procurement heads of contracting companies
Industry/Entity Type
Business

```html
<!DOCTYPE html>
<html lang="en">
<head>
<meta charset="UTF-8">
<title>Fleetwise Business Cards</title>
<link rel="stylesheet" href="https://fonts.googleapis.com/css2?family=Exo+2:wght@500;600;700&display=swap">
<style>
  :root {
    --stage: #2b2b2b;
    --green-deep: #1f7a36;
    --green: #2e8b3c;
    --green-mid: #43a047;
    --green-bright: #6cbf45;
    --lime: #8cc63f;
    --paper: #ffffff;
    --ink-green: #23773a;
  }
  * { margin: 0; padding: 0; box-sizing: border-box; }
  html, body {
    width: 1200px;
    height: 900px;
    overflow: hidden;
    background: var(--stage);
    font-family: "Exo 2", sans-serif;
  }
  .stage {
    position: relative;
    width: 1200px;
    height: 900px;
  }
  .card {
    position: absolute;
    left: 270px;
    width: 660px;
    height: 377px;
    overflow: hidden;
    box-shadow: 0 10px 30px rgba(0,0,0,0.45);
  }
  .card-front { top: 50px; background: var(--green); }
  .card-back { top: 473px; background: var(--paper); }
  .card-art {
    position: absolute;
    inset: 0;
    width: 100%;
    height: 100%;
  }
  .brand {
    position: absolute;
    display: flex;
    align-items: center;
    gap: 12px;
    font-weight: 700;
    letter-spacing: 0.5px;
  }
  .brand-dot {
    width: 22px;
    height: 22px;
    border-radius: 50%;
  }
  .card-front .brand {
    left: 190px;
    top: 150px;
    font-size: 58px;
    color: var(--paper);
  }
  .card-front .brand-dot { background: var(--paper); width: 30px; height: 30px; }
  .card-back .brand {
    right: 48px;
    top: 108px;
    font-size: 36px;
    color: var(--ink-green);
  }
  .card-back .brand-dot { background: var(--ink-green); }
  .holder {
    position: absolute;
    left: 44px;
    bottom: 58px;
  }
  .holder-name {
    display: inline-block;
    background: var(--lime);
    color: var(--paper);
    font-size: 30px;
    font-weight: 600;
    letter-spacing: 1.5px;
    padding: 1px 14px 0;
    border-radius: 6px;
    line-height: 1.15;
  }
  .holder-role {
    font-size: 19px;
    font-weight: 600;
    color: var(--ink-green);
    padding-left: 10px;
    line-height: 1.1;
  }
  .contact {
    position: absolute;
    right: 48px;
    bottom: 90px;
    color: var(--ink-green);
    font-size: 19px;
    line-height: 1.25;
    text-align: left;
  }
  .contact-phone { font-weight: 500; letter-spacing: 1px; }
  .contact-email { font-weight: 700; }
</style>
</head>
<body>
<main class="stage">

  <section class="card card-front" aria-label="Card front">
    <svg class="card-art" viewBox="0 0 660 377" preserveAspectRatio="none" aria-hidden="true">
      <defs>
        <linearGradient id="frontBase" x1="0" y1="0" x2="1" y2="1">
          <stop offset="0" stop-color="#4fb048"/>
          <stop offset="1" stop-color="#237d38"/>
        </linearGradient>
      </defs>
      <rect width="660" height="377" fill="url(#frontBase)"/>
      <path d="M0 250 C180 170 380 150 660 60 L660 0 L0 0 Z" fill="#ffffff" opacity="0.06"/>
      <path d="M0 377 C200 260 420 210 560 120 L660 90 L660 377 Z" fill="#1f7a36" opacity="0.35"/>
      <path d="M470 377 L660 160 L660 377 Z" fill="#8cc63f"/>
      <path d="M520 377 L660 230 L660 377 Z" fill="#a3d35a" opacity="0.6"/>
    </svg>
    <div class="brand"><span class="brand-dot"></span>Fleetwise</div>
  </section>

  <section class="card card-back" aria-label="Card back">
    <svg class="card-art" viewBox="0 0 660 377" preserveAspectRatio="none" aria-hidden="true">
      <path d="M0 0 L500 0 C380 40 260 120 160 180 C100 215 50 225 0 228 Z" fill="#2e8b3c"/>
      <path d="M0 0 L560 0 C420 30 300 90 200 140 C120 180 60 195 0 200 Z" fill="#43a047" opacity="0.85"/>
      <path d="M0 90 C150 70 320 40 460 30 C340 60 240 100 150 140 C90 165 40 175 0 178 Z" fill="#6cbf45"/>
      <path d="M150 95 C280 70 380 50 470 35 C390 55 310 80 230 105 Z" fill="#8cc63f" opacity="0.9"/>
    </svg>
    <div class="brand"><span class="brand-dot"></span>Fleetwise</div>
    <div class="holder">
      <div class="holder-name">NABIL HUSSAIN</div>
      <div class="holder-role">General manager</div>
    </div>
    <div class="contact">
      <div class="contact-phone">1 555 014 7392</div>
      <div class="contact-email">nabil@fleetwise-mail.com</div>
    </div>
  </section>

</main>
</body>
</html>
```